Standee design for an exhibition event

"Please read the details carefully:

80 cm (W) X 200 cm (H)
Res: 150dpi
output file : ai file.
Corporate Health Checkups
- Companies understand the importance of executive wellness for their employees. An unfit and unhealthy employee loses his productivity due to frequent absenteeism, lack of concentration and low energy levels at work. Regular health screening is the key to good employee health management.

```html
<!DOCTYPE html>
<html lang="en">
<head>
<meta charset="utf-8">
<title>Corporate Health Checkups Standee</title>
<link rel="stylesheet" href="https://fonts.googleapis.com/css2?family=Raleway:wght@500;600;700&family=Bebas+Neue&display=swap">
<style>
  :root {
    --stage: #3b3b3d;
    --header-grey: #cfcfd1;
    --footer-light: #d4d4d6;
    --footer-dark: #a8a8aa;
    --brand-green: #10806a;
    --white: #ffffff;
  }
  * { margin: 0; padding: 0; box-sizing: border-box; }
  html, body { width: 1200px; height: 1200px; overflow: hidden; }
  body {
    background: radial-gradient(circle at 50% 45%, #5a5a5c 0%, var(--stage) 70%);
    font-family: "Raleway", sans-serif;
  }
  .standee {
    position: absolute;
    left: 370px; top: 25px;
    width: 460px; height: 1150px;
    box-shadow: 0 6px 24px rgba(0,0,0,.45);
  }
  .standee-shapes { position: absolute; inset: 0; width: 460px; height: 1150px; }
  .brand {
    position: absolute; left: 0; top: 68px; width: 460px;
    display: flex; align-items: center; justify-content: center; gap: 12px;
  }
  .brand-mark {
    width: 22px; height: 22px; border-radius: 50%;
    background: var(--brand-green);
  }
  .brand-name {
    font-weight: 600; font-size: 34px; line-height: 1;
    color: var(--brand-green);
  }
  .headline {
    position: absolute; left: 0; top: 635px; width: 460px;
    text-align: center; color: var(--white); font-weight: 600; line-height: 1.2;
  }
  .headline-top { font-size: 41px; }
  .headline-main { font-size: 43px; }
  .intro {
    position: absolute; left: 24px; top: 754px; width: 414px;
    color: var(--white); font-size: 12.4px; font-weight: 500; line-height: 1.3;
  }
  .intro-line { display: block; text-align: justify; text-align-last: justify; }
  .intro-line.last { text-align-last: left; }
  .causes {
    position: absolute; left: 23px; top: 818px; width: 416px; height: 152px;
    border: 1px solid rgba(255,255,255,.85); border-radius: 10px;
    display: flex; justify-content: space-around; padding-top: 14px;
  }
  .cause { width: 130px; text-align: center; color: var(--white); }
  .cause-icon { width: 84px; height: 84px; display: block; margin: 0 auto 8px; }
  .cause-label { font-size: 13px; font-weight: 600; line-height: 1.3; text-transform: uppercase; }
  .closing {
    position: absolute; left: 0; top: 985px; width: 460px;
    text-align: center; color: var(--white);
    font-family: "Bebas Neue", sans-serif; font-size: 28px; line-height: 35px;
  }
</style>
</head>
<body>
  <div class="standee">
    <svg class="standee-shapes" viewBox="0 0 460 1150">
      <defs>
        <linearGradient id="photo-tone" x1="0" y1="0" x2="1" y2="1">
          <stop offset="0" stop-color="#e6ebee"/>
          <stop offset="0.35" stop-color="#6f8fc7"/>
          <stop offset="0.6" stop-color="#2d3138"/>
          <stop offset="1" stop-color="#7a5236"/>
        </linearGradient>
      </defs>
      <rect width="460" height="1150" fill="var(--header-grey)"/>
      <rect class="team-photo" x="0" y="130" width="460" height="500" fill="url(#photo-tone)"
            role="img" aria-label="Photo of a doctor and business executives reviewing health reports at a meeting table"/>
      <path class="header-band" d="M0 0 H460 V140 C390 158 300 190 225 190 C140 190 60 160 0 135 Z" fill="var(--header-grey)"/>
      <path d="M0 135 C60 160 140 190 225 190 C300 190 390 158 460 140" fill="none" stroke="var(--white)" stroke-width="3"/>
      <path d="M0 600 C110 578 200 565 260 568 C340 574 410 592 460 602" fill="none" stroke="var(--white)" stroke-width="4"/>
      <path class="green-panel" d="M0 612 C110 588 200 575 260 578 C340 584 410 602 460 612 V1092 H0 Z" fill="var(--brand-green)"/>
      <rect x="0" y="1092" width="230" height="58" fill="var(--footer-light)"/>
      <rect x="230" y="1092" width="230" height="58" fill="var(--footer-dark)"/>
    </svg>

    <div class="brand">
      <span class="brand-mark"></span>
      <span class="brand-name">Harbourview Hospital</span>
    </div>

    <h1 class="headline">
      <div class="headline-top">CORPORATE</div>
      <div class="headline-main">HEALTH CHECKUPS</div>
    </h1>

    <p class="intro">
      <span class="intro-line">Companies understand the importance of executive wellness for</span>
      <span class="intro-line">their employees. An unfit and unhealthy employee loses his</span>
      <span class="intro-line last">productivity due to</span>
    </p>

    <div class="causes">
      <div class="cause">
        <svg class="cause-icon" viewBox="0 0 84 84" fill="none" stroke="var(--white)" stroke-width="2">
          <circle cx="42" cy="42" r="40"/>
          <circle cx="28" cy="26" r="5" stroke-dasharray="2 2"/>
          <circle cx="56" cy="26" r="5" stroke-dasharray="2 2"/>
          <path d="M20 60 V40 Q20 34 28 34 Q36 34 36 40 V60" stroke-dasharray="2 2"/>
          <path d="M48 60 V40 Q48 34 56 34 Q64 34 64 40 V60" stroke-dasharray="2 2"/>
          <circle cx="42" cy="28" r="6"/>
          <path d="M33 64 V44 Q33 37 42 37 Q51 37 51 44 V64"/>
          <path d="M38 47 L41 50 L46 44"/>
        </svg>
        <div class="cause-label">Frequent<br>Absenteeism</div>
      </div>
      <div class="cause">
        <svg class="cause-icon" viewBox="0 0 84 84" fill="none" stroke="var(--white)" stroke-width="2">
          <circle cx="42" cy="42" r="40" fill="var(--white)" stroke="none"/>
          <path d="M24 42 C18 30 30 20 40 22 C50 16 66 24 62 38 C68 46 58 56 48 52 L54 66 L44 56 C34 58 22 52 24 42 Z" stroke="var(--brand-green)"/>
          <path d="M32 38 C38 30 48 44 52 34 M34 46 C42 40 46 50 54 44" stroke="var(--brand-green)"/>
        </svg>
        <div class="cause-label">Lack of<br>Concentration</div>
      </div>
      <div class="cause">
        <svg class="cause-icon" viewBox="0 0 84 84" fill="none" stroke="var(--white)" stroke-width="2">
          <circle cx="42" cy="42" r="40"/>
          <rect x="30" y="22" width="24" height="44" rx="3"/>
          <rect x="37" y="17" width="10" height="5"/>
          <path d="M45 27 L35 46 H42 L39 61 L50 40 H43 Z" fill="var(--white)"/>
        </svg>
        <div class="cause-label">Low Energy<br>Levels at Work</div>
      </div>
    </div>

    <div class="closing">
      Regular health screening<br>
      is the key to<br>
      good employee health management
    </div>
  </div>
</body>
</html>
```